May the Best Business Card Win

I want a business card that goes with the logo. We are an Energy Efficient Home Improvement Company. We want something modern but at the same time professional. This is going on a Black Matte Card so we want to impress everyone.

Front Side:

(Logo)
Lic:472159

Tomas J. Whitley
Founder & Energy Consultant
Tel: (818)555-0134
SolvaHomesCo@[login to view URL]
Cedarbrook CA 90577

Back Side:
Facebook Logo: SolvaHomesCo
Instagram Logo: SolvaHomesCo
Website Logo: [login to view URL]

Front Side:

(Logo)
Lic:472159

Helena Brochu
Lead Energy Consultant
Tel: (818)555-0192 Office: 818-555-0134
Email: Helenabrochu@[login to view URL]
Address: Cedarbrook CA 90577

Back Side:

```html
<!DOCTYPE html>
<html lang="en">
<head>
<meta charset="utf-8">
<title>Solva Homes – Business Card</title>
<link href="https://fonts.googleapis.com/css2?family=Roboto:wght@300;400;500&display=swap" rel="stylesheet">
<style>
  :root {
    --bg: #8e9093;
    --card: #1c1c1d;
    --green: #8cc63f;
    --white: #f2f2f2;
    --grey: #a9a9a9;
  }
  html, body {
    margin: 0;
    width: 1200px;
    height: 900px;
    overflow: hidden;
    background: var(--bg);
    font-family: "Roboto", Arial, sans-serif;
  }
  .canvas {
    position: relative;
    width: 1200px;
    height: 900px;
  }
  .card {
    position: absolute;
    left: 240px;
    width: 720px;
    height: 411px;
    background: var(--card);
    border-radius: 18px;
    overflow: hidden;
  }
  .card--info { top: 25px; }
  .card--brand { top: 464px; }

  .person {
    position: absolute;
    left: 52px;
    top: 52px;
  }
  .person__name {
    margin: 0;
    color: var(--green);
    font-size: 30px;
    font-weight: 400;
  }
  .person__title {
    margin: 6px 0 0;
    color: var(--grey);
    font-size: 16px;
    font-weight: 300;
  }
  .contact {
    list-style: none;
    margin: 20px 0 0;
    padding: 0;
  }
  .contact__item {
    display: flex;
    align-items: center;
    gap: 12px;
    color: var(--grey);
    font-size: 15px;
    font-weight: 300;
    margin-bottom: 9px;
  }
  .contact__icon { width: 15px; height: 15px; flex: none; }

  .wordmark {
    position: absolute;
    display: flex;
    flex-direction: column;
    align-items: center;
    gap: 12px;
  }
  .wordmark__dot {
    width: 64px;
    height: 64px;
    border-radius: 50%;
    background: var(--green);
  }
  .wordmark__name {
    color: var(--green);
    font-size: 26px;
    font-weight: 500;
    letter-spacing: 3px;
  }
  .card--info .wordmark { right: 60px; top: 120px; }
  .card--brand .wordmark { left: 50%; top: 115px; transform: translateX(-50%); }

  .divider {
    position: absolute;
    left: 300px;
    right: 60px;
    top: 266px;
    height: 2px;
    background: var(--green);
  }
  .address {
    position: absolute;
    right: 60px;
    top: 300px;
    display: flex;
    align-items: center;
    gap: 12px;
    color: var(--grey);
    font-size: 17px;
    font-weight: 300;
  }
  .address__pin { width: 18px; height: 24px; }

  .links {
    position: absolute;
    right: 46px;
    bottom: 40px;
    text-align: right;
  }
  .links__handle {
    display: flex;
    justify-content: flex-end;
    align-items: center;
    gap: 10px;
    color: var(--green);
    font-size: 16px;
    font-weight: 400;
    margin-bottom: 8px;
  }
  .links__square {
    width: 16px;
    height: 16px;
    background: var(--green);
    border-radius: 3px;
  }
  .links__web {
    color: var(--white);
    font-size: 16px;
    font-weight: 300;
  }
</style>
</head>
<body>
<main class="canvas">

  <section class="card card--info" aria-label="Business card, contact side">
    <div class="person">
      <h1 class="person__name">Tomas J. Whitley</h1>
      <p class="person__title">Founder &amp; Energy Consultant</p>
      <ul class="contact">
        <li class="contact__item">
          <svg class="contact__icon" viewBox="0 0 24 24" aria-hidden="true"><path fill="#8cc63f" d="M6.6 10.8a15.2 15.2 0 0 0 6.6 6.6l2.2-2.2c.3-.3.7-.4 1-.2 1.1.4 2.3.6 3.6.6.6 0 1 .4 1 1V20c0 .6-.4 1-1 1A17 17 0 0 1 3 4c0-.6.4-1 1-1h3.5c.6 0 1 .4 1 1 0 1.3.2 2.5.6 3.6.1.3 0 .7-.2 1z"/></svg>
          818-555-0134
        </li>
        <li class="contact__item">
          <svg class="contact__icon" viewBox="0 0 24 24" aria-hidden="true"><path fill="#8cc63f" d="M3 5h18v14H3z"/><path fill="none" stroke="#1c1c1d" stroke-width="2" d="M3 6l9 7 9-7"/></svg>
          SolvaHomesCo@postbox.com
        </li>
        <li class="contact__item">
          <svg class="contact__icon" viewBox="0 0 24 24" aria-hidden="true"><g fill="none" stroke="#8cc63f" stroke-width="2"><circle cx="12" cy="12" r="9"/><path d="M3 12h18M12 3c3 3 3 15 0 18M12 3c-3 3-3 15 0 18"/></g></svg>
          www.SolvaHomesCo.com
        </li>
      </ul>
    </div>

    <div class="wordmark">
      <span class="wordmark__dot"></span>
      <span class="wordmark__name">SOLVA HOMES</span>
    </div>

    <div class="divider"></div>

    <div class="address">
      <svg class="address__pin" viewBox="0 0 18 24" aria-hidden="true"><path fill="#8cc63f" d="M9 0a9 9 0 0 0-9 9c0 6.5 9 15 9 15s9-8.5 9-15a9 9 0 0 0-9-9zm0 12.5A3.5 3.5 0 1 1 9 5.5a3.5 3.5 0 0 1 0 7z"/></svg>
      Cedarbrook CA 90577
    </div>
  </section>

  <section class="card card--brand" aria-label="Business card, brand side">
    <div class="wordmark">
      <span class="wordmark__dot"></span>
      <span class="wordmark__name">SOLVA HOMES</span>
    </div>

    <div class="links">
      <div class="links__handle">SolvaHomesCo <span class="links__square"></span></div>
      <div class="links__web">www.SolvaHomesCo.com</div>
    </div>
  </section>

</main>
</body>
</html>
```